Webdesign für Frauen-Personal-Training
Sehr schnelle Umsetzung meiner Wünsche und Ideen
Zielgruppe
Personal Training für Frauen in Führungspositionen ab 30 Jahren
Aufgabenstellung
Bilderwelt stimmig, Farbfokus auf CI Farben (im Anhang wie auch Logo), 1/3 Text, 2/3 Bilderwelt
- Hamburger Menü, kein klassisches
- Footer: Anschrift, Datenschutz, Impressum
- Headerimage mit Seitentitel im Bild, Titelunterschrift 2/3 der Bildschirmhöhe
- Berücksichtigung von Whitespace
- Verwendung von Icons zum Beispiel auf der Startseite beim Punkt 'du suchst - ich biete'
Seiten:
- Startseite: Einstieg für Besucher der Homepage in der Richtung 'du suchst, ich biete', abschließend Formular --> Abschluss Kontaktformular
- Training: Trainingsweise und Arbeitsweise beschreiben
- Über mich (Aufbau der Seite gleich wie 'Training' und 'Preise'): Professionelle Erfahrungen in Richtung training, Ernährung, Gesundheit --> Abschluss: CTA 'Nimm Kontakt zu mir auf und informiere dich in einem persönlichen Gespräch --> Link auf Kontaktseite
- Räumlichkeiten --> Abschluss: CTA 'Nimm Kontakt zu mir auf und informiere dich in einem persönlichen Gespräch --> Link auf Kontaktseite
- Preise --> Abschluss: CTA 'Nimm Kontakt zu mir auf und informiere dich in einem persönlichen Gespräch --> Link auf Kontaktseite
- Kontaktseite (Landing Page)
(- Impressum / Datenschutzseite)
Beispielseite:
https://www.quintello.com/rastavoni

```html
<!DOCTYPE html>
<html lang="de">
<head>
<meta charset="utf-8">
<title>Formwerk – Personal Training für Frauen</title>
<link href="https://fonts.googleapis.com/css2?family=Exo+2:wght@400;500&family=Rubik:wght@400;500&display=swap" rel="stylesheet">
<style>
:root{
  --olive:#7a735b;
  --green:#629b76;
  --green-text:#4f9a6c;
  --grey:#eeeeee;
  --ink:#222222;
  --body:#555555;
  --white:#ffffff;
}
*{margin:0;padding:0;box-sizing:border-box}
html,body{width:1200px;height:3812px;overflow:hidden;background:var(--white)}
body{position:relative;font-family:"Rubik",sans-serif;color:var(--ink)}
.abs{position:absolute}
.display{font-family:"Exo 2",sans-serif;font-weight:400;color:var(--ink);line-height:1.02}
.eyebrow{font-size:14px;color:var(--green-text);text-transform:uppercase;letter-spacing:.2px}
.copy{font-size:11px;line-height:22.4px;color:var(--body)}
.btn{background:var(--green);color:var(--white);font-size:12px;font-weight:500;letter-spacing:1.6px;display:flex;align-items:center;justify-content:center;text-transform:uppercase}
.photo{border:0}
.quote-box{background:var(--green);color:var(--white);font-family:"Rubik",sans-serif;font-size:19px;line-height:30px;padding:28px 26px}
.stat{width:180px;text-align:center}
.stat-num{font-family:"Exo 2",sans-serif;font-size:27px;color:var(--ink);margin-top:12px}
.stat-cap{font-size:12px;line-height:19px;color:var(--body);margin-top:8px}
.card-label{background:var(--white);font-family:"Exo 2",sans-serif;font-size:18px;line-height:21px;color:var(--ink)}
.footer-link{font-size:9px;font-weight:500;letter-spacing:1.2px;color:var(--white);text-transform:uppercase}
</style>
</head>
<body>

<!-- Header / Hero -->
<div class="abs" style="left:484px;top:0;width:716px;height:648px;background:var(--olive)"></div>
<div class="abs" style="left:93px;top:12px;display:flex;align-items:center;gap:8px">
  <span style="width:12px;height:12px;border-radius:50%;background:var(--green)"></span>
  <span style="font-family:'Rubik',sans-serif;font-size:20px;font-weight:500;color:var(--green)">Formwerk</span>
</div>
<div class="abs" style="left:93px;top:40px;font-size:8px;color:var(--green)">Personal Training für Frauen</div>
<svg class="abs" style="left:1076px;top:26px" width="28" height="12" aria-label="Menü"><rect y="0" width="28" height="2" fill="#fff"/><rect y="9" width="28" height="2" fill="#fff"/></svg>

<div class="abs photo" role="img" aria-label="Lächelnde Frau im blauen Kleid vor Bürogebäuden" style="left:93px;top:62px;width:1013px;height:531px;background:linear-gradient(100deg,#e6e8ea 0%,#d5dade 40%,#8fa3b8 70%,#556d8c 100%)"></div>
<div class="abs eyebrow" style="left:232px;top:240px">Unsere Strategie</div>
<div class="abs display" style="left:231px;top:266px;font-size:40px;line-height:40px;width:380px">Der schnellste Weg zu Ihrer glücklichen Karriere</div>
<div class="abs btn" style="left:234px;top:418px;width:168px;height:40px">Mehr Info</div>
<svg class="abs" style="left:232px;top:614px" width="180" height="14">
  <line x1="2" y1="7" x2="48" y2="7" stroke="#bbb"/><polyline points="6,4 2,7 6,10" fill="none" stroke="#bbb"/>
  <circle cx="68" cy="7" r="4" fill="none" stroke="#999"/><circle cx="68" cy="7" r="1.5" fill="#555"/>
  <circle cx="89" cy="7" r="2" fill="#bbb"/><circle cx="109" cy="7" r="2" fill="#bbb"/>
  <line x1="128" y1="7" x2="176" y2="7" stroke="#333"/><polyline points="172,4 176,7 172,10" fill="none" stroke="#333"/>
</svg>

<!-- Über mich -->
<div class="abs eyebrow" style="left:232px;top:771px">Über mich</div>
<div class="abs display" style="left:231px;top:798px;font-size:40px;line-height:40px">Meine persönliche<br>Geschichte</div>
<p class="abs copy" style="left:421px;top:914px;width:550px">Ich möchte ein wenig über meine persönliche Geschichte erzählen, die mich dazu veranlasste, Frauen zu helfen, „mutig zu sein“ und einen wahren Durchbruch zu erzielen, um ihr höchstes und bestes Potenzial und ihre aufregendsten Visionen für ihr Leben und ihre Arbeit zu erreichen. Als ich mich 40 Jahren näherte, begannen sich die Dinge zu ändern. Ich war äußerlich sehr "erfolgreich", aber innerlich kämpfte ich tief. Die meiste Zeit fühlte sich meine Arbeit falsch und unecht an, und die Vereinbarkeit von Beruf und Familie war unerreichbar. Ich konnte nicht wahrheitsgemäß sprechen oder mein wahres Selbst sein.</p>
<div class="abs photo" role="img" aria-label="Geschäftlicher Händedruck vor Hochhäusern" style="left:420px;top:1098px;width:546px;height:312px;background:linear-gradient(90deg,#4d5b86 0%,#c9d2dc 45%,#9fb2c8 75%,#3b4f7a 100%)"></div>
<div class="abs quote-box" style="left:234px;top:1248px;width:294px;height:213px;padding-top:30px">Mit unseren Spezialisten und Experten, die Ihnen zur Verfügung stehen, werden Sie komplexe Probleme mit Zuversicht angehen</div>

<!-- Vorteile -->
<div class="abs" style="left:0;top:1586px;width:716px;height:456px;background:var(--grey)"></div>
<div class="abs eyebrow" style="left:232px;top:1708px">Beratungsleistungen</div>
<div class="abs display" style="left:231px;top:1736px;font-size:40px">Person Vorteile</div>
<p class="abs copy" style="left:233px;top:1813px;width:540px">Als Karriere-Erfolgstrainerin, die mutige Expertin und Autorin für Nordblatt, Stadtkurier und Netzwerkplatz und andere Plattformen findet, konzentriere ich mich intensiv darauf, professionellen Frauen dabei zu helfen, „tief zu graben, ihre richtige Arbeit zu entdecken und die Welt damit zu erleuchten“ liebe meine Arbeit und werde von ihr außerordentlich erfüllt und engagiere mich jeden Tag leidenschaftlich dafür, anderen Frauen zu helfen.</p>

<div class="abs" style="left:599px;top:1955px;width:1px;height:122px;background:#e2e2e2"></div>
<div class="abs" style="left:788px;top:1955px;width:1px;height:122px;background:#e2e2e2"></div>
<div class="abs stat" style="left:415px;top:1958px">
  <svg width="40" height="38" viewBox="0 0 40 38" fill="none" stroke="#629b76" stroke-width="1.4"><circle cx="18" cy="20" r="15"/><circle cx="18" cy="20" r="9"/><circle cx="18" cy="20" r="3"/><line x1="18" y1="20" x2="36" y2="4"/><polyline points="31,3 36,4 35,9"/></svg>
  <div class="stat-num">1024</div><div class="stat-cap">Menschen haben Ziele<br>erreicht</div>
</div>
<div class="abs stat" style="left:603px;top:1958px">
  <svg width="40" height="38" viewBox="0 0 40 38" fill="none" stroke="#629b76" stroke-width="1.4"><rect x="3" y="9" width="34" height="26" rx="2"/><rect x="14" y="3" width="12" height="6"/><line x1="3" y1="19" x2="37" y2="19"/><rect x="17" y="16" width="6" height="7"/></svg>
  <div class="stat-num">81</div><div class="stat-cap">strategische Partner<br>gewonnen</div>
</div>
<div class="abs stat" style="left:792px;top:1958px">
  <svg width="40" height="38" viewBox="0 0 40 38" fill="none" stroke="#629b76" stroke-width="1.4"><circle cx="20" cy="19" r="12"/><circle cx="20" cy="19" r="5"/><line x1="20" y1="2" x2="20" y2="7"/><line x1="20" y1="31" x2="20" y2="36"/><line x1="3" y1="19" x2="8" y2="19"/><line x1="32" y1="19" x2="37" y2="19"/><line x1="8" y1="7" x2="11" y2="10"/><line x1="29" y1="28" x2="32" y2="31"/><line x1="32" y1="7" x2="29" y2="10"/><line x1="8" y1="31" x2="11" y2="28"/></svg>
  <div class="stat-num">219</div><div class="stat-cap">Menschen wechselten die<br>Berufsrichtung</div>
</div>

<!-- Kurse -->
<div class="abs" style="left:232px;top:2202px;width:62px;height:3px;background:var(--green)"></div>
<div class="abs display" style="left:231px;top:2218px;font-size:40px">Unsere Kurse</div>

<div class="abs" style="left:280px;top:2500px;width:330px;height:113px;background:var(--olive)"></div>
<div class="abs photo" role="img" aria-label="Team legt die Hände übereinander" style="left:234px;top:2303px;width:357px;height:254px;background:linear-gradient(135deg,#c7c9d6 0%,#8a90a8 45%,#d9c77a 100%)"></div>
<div class="abs card-label" style="left:297px;top:2503px;width:313px;height:90px;padding:28px 0 0 21px">Teambuilding und<br>Teammanagement<br>Online Kurse</div>
<svg class="abs" style="left:541px;top:2550px" width="50" height="8"><line x1="0" y1="4" x2="48" y2="4" stroke="#629b76"/><polyline points="44,1 48,4 44,7" fill="none" stroke="#629b76"/></svg>

<div class="abs" style="left:609px;top:2600px;width:60px;height:57px;background:var(--grey)"></div>
<div class="abs photo" role="img" aria-label="Hände mit Tablet und Diagrammen am Schreibtisch" style="left:609px;top:2403px;width:357px;height:199px;background:linear-gradient(120deg,#e8e6e2 0%,#c9c6c0 50%,#7d7a74 100%)"></div>
<div class="abs card-label" style="left:669px;top:2602px;width:297px;height:58px;padding:20px 0 0 24px">Betriebsführung und<br>strategische Planung</div>
<svg class="abs" style="left:916px;top:2643px" width="50" height="8"><line x1="0" y1="4" x2="48" y2="4" stroke="#629b76"/><polyline points="44,1 48,4 44,7" fill="none" stroke="#629b76"/></svg>

<p class="abs copy" style="left:422px;top:2724px;width:535px">Machen Sie mit, ohne ein Unternehmen zu haben, finden Sie Ihren Mitbegründer und beginnen Sie mit der Unterstützung unseres globalen Netzwerks von Grund auf neu zu bauen. Wählen Sie eine unserer Städte aus und bereiten Sie sich auf eine Reise vor, die Sie an Orte führt, die Sie nicht für möglich gehalten haben.</p>
<div class="abs btn" style="left:423px;top:2856px;width:168px;height:40px">Mehr Info</div>

<!-- Profil -->
<div class="abs photo" role="img" aria-label="Porträt der Trainerin im blauen Kleid im Büro" style="left:234px;top:3020px;width:482px;height:338px;background:linear-gradient(90deg,#f2f2f0 0%,#e4e4e2 40%,#3f4f78 60%,#d8d8d6 100%)"></div>
<div class="abs copy" style="left:734px;top:3060px;line-height:22px">Mara Lindqvist<br>Gründer</div>
<div class="abs copy" style="left:734px;top:3132px">Berlin 2019</div>
<div class="abs quote-box" style="left:672px;top:3197px;width:294px;height:213px">Nimm Kontakt zu mir auf und informiere dich in einem persönlichen Gespräch</div>
<svg class="abs" style="left:888px;top:3370px" width="50" height="8"><line x1="0" y1="4" x2="48" y2="4" stroke="#fff"/><polyline points="44,1 48,4 44,7" fill="none" stroke="#fff"/></svg>

<!-- CTA band -->
<div class="abs" style="left:0;top:3530px;width:1200px;height:222px;background:var(--grey)"></div>
<div class="abs" style="left:0;top:3590px;width:1200px;text-align:center;font-family:'Exo 2',sans-serif;font-size:18px;color:var(--ink)">Professionelle Erfahrungen in Richtung training, Ernährung, Gesundheit</div>
<div class="abs btn" style="left:506px;top:3647px;width:187px;height:40px">Kontakt zu mir</div>

<!-- Footer -->
<div class="abs" style="left:0;top:3752px;width:1200px;height:60px;background:var(--olive)"></div>
<div class="abs footer-link" style="left:233px;top:3777px">Impressum</div>
<div class="abs footer-link" style="left:322px;top:3777px">Datenschutzseite</div>
<div class="abs" style="left:868px;top:3777px;font-size:8px;color:var(--white)">© Formwerk 2019</div>

</body>
</html>
```